Eye Doctor Needs Updated Business Card

We need a standard US business card designed for an optometrist's practice. Our practice name is Halvorn Vision Center and attached you'll find our logos. We are located in a smaller community, we are a trusted source for eye care and designer eyewear. We have 2 different version of our logos, so both versions are attached. Our slogan is "Close to Home, Clear in Every View". I'd like to see designs with one of our logos on the front with our contact info, and have the slogan on the back by itself. Final design should be professional looking, include the colors of our logo or colors that compliment the logo. We want it to look appropriate for a healthcare practice but also up-to-date, eye-catching, to have the normal contact info like address, phone #, email, but also possibly room for additional contact info such as facebook.
Updates

I just uploaded .eps files to use instead of the jpeg. Hope that helps!

So many great designs! We tending to like the darker blues that are used in our logo as the main blue color for the business cards. We also really like the use of a water-mark type appearance on either the front and/or back, or the embossed look as well looks nice. Thank you all for such great designs!

We're preferring the designs where white and the darker blue used in our logo are the primary colors on the front, but with a little green used as well. Again though, thanks for all the impressive designs so far!

Industry/Entity Type

Healthcare

```html
<!DOCTYPE html>
<html lang="en">
<head>
<meta charset="utf-8">
<title>Halvorn Vision Center – Business Cards</title>
<link rel="stylesheet" href="https://fonts.googleapis.com/css2?family=Open+Sans:wght@400;600;700&family=Bitter:wght@400&display=swap">
<style>
  :root {
    --navy: #0d2c8c;
    --navy-deep: #0a237a;
    --blue-mid: #1f5fae;
    --blue-glow: #4aa8e6;
    --green: #5bb227;
    --white: #ffffff;
    --stage: #eceef1;
    --label: #3a3f48;
  }
  * { box-sizing: border-box; margin: 0; padding: 0; }
  html, body {
    width: 1200px; height: 798px; overflow: hidden;
    background: var(--stage);
    font-family: "Open Sans", Arial, sans-serif;
  }
  .sheet { position: relative; width: 1200px; height: 798px; }

  .card { position: absolute; overflow: hidden; box-shadow: 0 2px 8px rgba(0,0,0,.18); }

  /* Front */
  .card-front { left: 326px; top: 38px; width: 548px; height: 311px; background: var(--white); }
  .card-front .wave { position: absolute; inset: 0; width: 100%; height: 100%; }
  .front-mark {
    position: absolute; left: 0; right: 0; top: 24px;
    display: flex; flex-direction: column; align-items: center; gap: 12px;
  }
  .front-mark .dot { width: 66px; height: 66px; border-radius: 50%; background: var(--green); }
  .front-mark .name { font-weight: 700; font-size: 22px; color: var(--navy); letter-spacing: .3px; }

  .front-person {
    position: absolute; left: 10px; width: 242px; top: 220px;
    text-align: right; color: var(--white);
  }
  .front-person .person-name { font-size: 20px; font-weight: 700; line-height: 1.1; }
  .front-person .person-name span { font-weight: 400; font-size: 16px; }
  .front-person .address { margin-top: 12px; font-size: 14.5px; line-height: 1.4; }

  .front-divider {
    position: absolute; left: 274px; top: 210px; width: 1px; height: 90px;
    background: rgba(255,255,255,.7);
  }
  .front-contacts {
    position: absolute; left: 292px; top: 208px;
    list-style: none; color: var(--white); font-size: 15px; line-height: 21.5px;
  }
  .front-contacts li { display: flex; align-items: center; gap: 5px; white-space: nowrap; }
  .front-contacts svg { width: 11px; height: 11px; flex: none; }

  /* Backs */
  .card-back {
    width: 548px; height: 313px;
    background: radial-gradient(ellipse 58% 62% at 50% 50%, var(--blue-glow) 0%, var(--blue-mid) 45%, var(--navy) 85%, var(--navy-deep) 100%);
    color: var(--white); text-align: center;
    display: flex; flex-direction: column; align-items: center; justify-content: center;
  }
  .back-one { left: 40px; top: 370px; }
  .back-two { left: 603px; top: 378px; }
  .back-one .dot { width: 98px; height: 98px; border-radius: 50%; background: var(--white); margin-top: 10px; margin-bottom: 16px; }
  .card-back .name { font-weight: 700; font-size: 30px; letter-spacing: .4px; line-height: 1.2; }
  .card-back .slogan { font-family: "Bitter", Georgia, serif; font-size: 19.5px; margin-top: 14px; }
  .back-two .name { font-size: 33px; }
  .back-two .slogan { font-size: 20px; margin-top: 16px; }

  .card-label { position: absolute; font-size: 29px; color: var(--label); }
  .label-one { left: 239px; top: 686px; }
  .label-two { left: 840px; top: 692px; }
</style>
</head>
<body>
<main class="sheet">

  <section class="card card-front" aria-label="Card front">
    <svg class="wave" viewBox="0 0 548 311" preserveAspectRatio="none" aria-hidden="true">
      <defs>
        <radialGradient id="frontBlue" cx="50%" cy="75%" r="60%">
          <stop offset="0" stop-color="#3f8fd0"/>
          <stop offset="1" stop-color="#1a4f8f"/>
        </radialGradient>
      </defs>
      <path d="M0 118 Q274 240 548 118 L548 311 L0 311 Z" fill="var(--green)"/>
      <path d="M0 136 Q274 250 548 128 L548 311 L0 311 Z" fill="var(--white)"/>
      <path d="M0 144 Q274 256 548 136 L548 311 L0 311 Z" fill="url(#frontBlue)"/>
    </svg>

    <div class="front-mark">
      <span class="dot" aria-hidden="true"></span>
      <span class="name">Halvorn Vision Center</span>
    </div>

    <div class="front-person">
      <p class="person-name">Your Name, <span>Title</span></p>
      <p class="address">Street Name, City Name<br>State Zipcode</p>
    </div>

    <div class="front-divider" aria-hidden="true"></div>

    <ul class="front-contacts">
      <li><svg viewBox="0 0 10 10" aria-hidden="true"><rect width="10" height="10" rx="1" fill="#ffffff"/></svg>/halvornvision.com</li>
      <li><svg viewBox="0 0 12 12" aria-hidden="true"><circle cx="6" cy="6" r="5.3" fill="none" stroke="#fff" stroke-width="1.2"/><path d="M4 3.2 L5.2 3 L5.6 5 L4.8 5.5 Q5.5 7 6.6 7.4 L7.1 6.6 L9 7.1 L8.8 8.3 Q6 8.6 3.8 5.4 Z" fill="#fff"/></svg>123-456-7890</li>
      <li><svg viewBox="0 0 12 12" aria-hidden="true"><rect x="1" y="3" width="10" height="7" fill="#fff"/><path d="M1 3 L6 7 L11 3" fill="none" stroke="#1d5a9c" stroke-width="1"/></svg>halvornvision@gmail.com</li>
      <li><svg viewBox="0 0 12 12" aria-hidden="true"><circle cx="6" cy="6" r="5" fill="none" stroke="#fff" stroke-width="1.1"/><ellipse cx="6" cy="6" rx="2.2" ry="5" fill="none" stroke="#fff" stroke-width="1"/><path d="M1 6 H11" stroke="#fff" stroke-width="1"/></svg>www.halvornvision.com</li>
    </ul>
  </section>

  <section class="card card-back back-one" aria-label="Card back, version one">
    <span class="dot" aria-hidden="true"></span>
    <p class="name">Halvorn Vision Center</p>
    <p class="slogan">Close to Home, Clear in Every View</p>
  </section>
  <p class="card-label label-one">Back -1</p>

  <section class="card card-back back-two" aria-label="Card back, version two">
    <p class="name">Halvorn Vision Center</p>
    <p class="slogan">Close to Home, Clear in Every View</p>
  </section>
  <p class="card-label label-two">Back -2</p>

</main>
</body>
</html>
```